Disability Support service provider Needs a shopfront graphic Design

We are based in Sydney, Australia. Our company is called 'Coral Step Care Services'. We provide care services to anyone with a disability. I would like to see designs that are colourful and perhaps transparent. The colours from my logo uploaded can be used as a guide. I would also like a bit of information about our services on the design somewhere maybe in point form, for eg. Disability Support Services, We are people helping People, take control of your disability, supporting people to live the life they want to live, I would like the design to be friendly and inviting.

```html
<!DOCTYPE html>
<html lang="en">
<head>
<meta charset="utf-8">
<title>Coral Step Care Services – Shopfront Banner</title>
<link rel="stylesheet" href="https://fonts.googleapis.com/css2?family=Jost:wght@500;600&display=swap">
<style>
  :root {
    --backdrop: #c4c4c4;
    --backdrop-light: #e6e6e6;
    --banner-bg: #ffffff;
    --sun-yellow: #f4d67a;
    --sky-blue: #8fa6d6;
    --leaf-green: #3fa366;
    --lime: #bfdc74;
    --lime-deep: #8cc46a;
    --maroon: #6a2a26;
  }
  * { margin: 0; padding: 0; box-sizing: border-box; }
  html, body {
    width: 1200px;
    height: 480px;
    overflow: hidden;
  }
  body {
    position: relative;
    background: radial-gradient(ellipse at center, var(--backdrop-light) 0%, var(--backdrop) 75%);
    font-family: "Jost", "Futura", sans-serif;
    color: var(--maroon);
  }
  .banner {
    position: absolute;
    left: 92px;
    top: 86px;
    width: 1016px;
    height: 288px;
    background: var(--banner-bg);
    overflow: hidden;
    box-shadow: 0 2px 6px rgba(0,0,0,0.12);
  }
  .banner-shapes {
    position: absolute;
    inset: 0;
    width: 1016px;
    height: 288px;
  }
  .brand-name {
    position: absolute;
    left: 358px;
    top: 14px;
    width: 300px;
    text-align: center;
    font-weight: 500;
    color: var(--maroon);
    text-transform: uppercase;
    line-height: 1;
  }
  .brand-name .line-main {
    display: block;
    font-size: 31px;
    letter-spacing: 1.5px;
  }
  .brand-name .line-sub {
    display: block;
    margin-top: 7px;
    font-size: 22px;
    letter-spacing: 4px;
  }
  .service-point {
    position: absolute;
    transform: translate(-50%, -50%);
    text-align: center;
    color: var(--maroon);
    font-weight: 600;
  }
  .service-point--disability {
    left: 304px;
    top: 186px;
    font-size: 19px;
    line-height: 1.35;
  }
  .service-point--helping {
    left: 508px;
    top: 182px;
    font-size: 23px;
    line-height: 1.35;
    width: 200px;
  }
  .service-point--life {
    left: 712px;
    top: 184px;
    font-size: 15px;
    font-weight: 500;
    line-height: 1.4;
    width: 190px;
  }
</style>
</head>
<body>
  <section class="banner" aria-label="Coral Step Care Services shopfront banner">
    <svg class="banner-shapes" viewBox="0 0 1016 288" aria-hidden="false">
      <defs>
        <radialGradient id="emblem-fill" cx="50%" cy="55%" r="55%">
          <stop offset="0%" stop-color="#9fce6e"/>
          <stop offset="70%" stop-color="#c6e08a"/>
          <stop offset="100%" stop-color="#d6e9a6"/>
        </radialGradient>
      </defs>
      <circle class="sun-circle" cx="508" cy="8" r="172" fill="var(--sun-yellow)" opacity="0.85"/>
      <circle class="overlap-blue" cx="405" cy="186" r="100" fill="var(--sky-blue)" opacity="0.7"/>
      <circle class="overlap-blue" cx="611" cy="186" r="100" fill="var(--sky-blue)" opacity="0.7"/>
      <circle class="overlap-lime" cx="304" cy="186" r="100" fill="var(--lime)" opacity="0.72"/>
      <circle class="overlap-lime" cx="712" cy="186" r="100" fill="var(--lime)" opacity="0.72"/>
      <circle class="overlap-green" cx="508" cy="186" r="100" fill="var(--leaf-green)" opacity="0.7"/>
      <g role="img" aria-label="Decorative leafy tree and figure illustration, left">
        <circle cx="100" cy="180" r="112" fill="url(#emblem-fill)"/>
      </g>
      <g role="img" aria-label="Decorative leafy tree and figure illustration, right">
        <circle cx="916" cy="180" r="112" fill="url(#emblem-fill)"/>
      </g>
    </svg>

    <h1 class="brand-name">
      <span class="line-main">Coral Step</span>
      <span class="line-sub">Care Services</span>
    </h1>

    <p class="service-point service-point--disability">Disability<br>Support<br>Services</p>
    <p class="service-point service-point--helping">We are<br>people helping<br>People</p>
    <p class="service-point service-point--life">supporting people<br>to live the life<br>they want to live</p>
  </section>
</body>
</html>
```